Pellridge Glassware Brand Design

Logo Design Brief

Pellridge Glassware is a startup premium drinkware company launching its first product - a premium grade 24oz Copa de Balon Gin Glass.

We are looking for branding design to produce our logo and the label for our first product; a premium 24oz Copa de Balon Gin Glass.

Design Brief for logo:

• Premium brand
• Modern, elegant and sleek design
• Not busy
• Logo does not have to include reference to drinkware

Label Design Brief:

A label design for our packaging - The packaging is tubular and will house 2 gin glasses for retail sale. The label will be stuck on the front of the tube and will need to excite people about the purchase they have just made with Pellridge Glassware.
The label design needs to incorporate the logo and reflect our premium brand image.

• The label size is 460mm x 150mm

• Label must have modern and sleek look and must not look busy.

• The label will need to work well in both multicolour and single colour print.

• Please see attached Barcode, this will need to be incorporated into the label. Barcode will need to be 300dpi or higher and 381mm x 254mm to be scannable on the packaging.

• Please see attached pictures of the tubular packaging the label is going on to

Please also see attached 3 images of the glasses being sold - This is for reference only.
Updates

Design period has been extended for 5 Days, please ensure both a logo and corresponding packaging design is submitted. Thank you Added Wednesday, October 4, 2017

Target Market(s)

Gin Drinkers - Premium - Male and Female - All ages above 18

Industry/Entity Type

It Company

Logo Text

Pellridge

Font styles to use
Serif
Sans Serif

Colors

Designer to choose colors to be used in the design.

Requirements
Must have
• Sleek modern design. Logo and Label must be submitted on this project.
Should not have
• Do not make this a busy logo or label

```html
<!DOCTYPE html>
<html lang="en">
<head>
<meta charset="utf-8">
<title>Pellridge Glassware – Gin Glass Labels</title>
<link rel="stylesheet" href="https://fonts.googleapis.com/css2?family=Montserrat:wght@400&family=Quicksand:wght@300&family=Roboto+Condensed:ital,wght@0,400;1,400&family=Oswald:wght@400&display=swap">
<style>
  :root {
    --page: #ffffff;
    --label: #000000;
    --ink: #ffffff;
    --art-light: #d9d9d9;
    --art-dark: #3a3a3a;
  }
  html, body {
    margin: 0;
    padding: 0;
    width: 1200px;
    height: 1128px;
    overflow: hidden;
    background: var(--page);
  }
  .canvas {
    position: relative;
    width: 1200px;
    height: 1128px;
  }
  .label {
    position: absolute;
    top: 199px;
    width: 248px;
    height: 759px;
    background: var(--label);
    color: var(--ink);
    overflow: hidden;
  }
  .label--script { left: 278px; }
  .label--bold { left: 708px; }

  .brand-mark {
    position: absolute;
    left: 50%;
    top: 80px;
    width: 52px;
    height: 52px;
    margin-left: -27px;
    border: 1.5px solid var(--ink);
    border-radius: 50%;
  }
  .brand {
    position: absolute;
    left: 0;
    right: 0;
    top: 200px;
    text-align: center;
    font-family: "Montserrat", sans-serif;
    font-weight: 400;
    line-height: 1.3;
  }
  .brand__name {
    display: block;
    font-size: 17px;
    letter-spacing: 4px;
    margin-right: -4px;
  }
  .brand__line {
    display: block;
    font-size: 10px;
    letter-spacing: 3px;
    margin-right: -3px;
  }

  .product-title--script {
    position: absolute;
    left: 33px;
    top: 290px;
    margin: 0;
    font-family: "Quicksand", sans-serif;
    font-weight: 300;
    font-size: 56px;
    line-height: 64px;
  }
  .volume {
    position: absolute;
    font-family: "Roboto Condensed", sans-serif;
    font-size: 18px;
    letter-spacing: 1px;
    white-space: nowrap;
  }
  .label--script .volume { right: 44px; top: 440px; font-style: italic; }
  .label--bold .volume { right: 18px; top: 503px; }

  .product-title--bold {
    position: absolute;
    left: 0;
    right: 0;
    top: 260px;
    margin: 0;
    text-align: center;
    font-family: "Oswald", sans-serif;
    font-weight: 400;
    font-size: 50px;
    line-height: 1;
    letter-spacing: -0.5px;
  }

  .art {
    position: absolute;
    left: 0;
    bottom: 0;
    display: block;
  }
</style>
</head>
<body>
<main class="canvas">

  <section class="label label--script">
    <div class="brand-mark"></div>
    <div class="brand">
      <span class="brand__name">PELLRIDGE</span>
      <span class="brand__line">GLASSWARE</span>
    </div>
    <h1 class="product-title--script">Gin<br>Glass</h1>
    <span class="volume">24oz</span>
    <svg class="art" width="248" height="300" viewBox="0 0 248 300" role="img" aria-label="Black and white illustration of flowing liquid streams with bubbles">
      <defs>
        <linearGradient id="flow-left" x1="0" y1="0" x2="1" y2="1">
          <stop offset="0" stop-color="var(--art-light)"/>
          <stop offset="1" stop-color="var(--art-dark)"/>
        </linearGradient>
      </defs>
      <path d="M0 126 C60 110 120 80 170 60 C200 45 230 30 248 12 L248 300 L0 300 Z" fill="url(#flow-left)"/>
    </svg>
  </section>

  <section class="label label--bold">
    <div class="brand-mark"></div>
    <div class="brand">
      <span class="brand__name">PELLRIDGE</span>
      <span class="brand__line">GLASSWARE</span>
    </div>
    <h1 class="product-title--bold">Gin Glass</h1>
    <svg class="art" width="248" height="420" viewBox="0 0 248 420" role="img" aria-label="Black and white marbled swirl pattern">
      <defs>
        <linearGradient id="flow-right" x1="0" y1="0" x2="1" y2="1">
          <stop offset="0" stop-color="var(--art-light)"/>
          <stop offset="1" stop-color="var(--art-dark)"/>
        </linearGradient>
      </defs>
      <path d="M0 0 C90 4 180 14 248 30 L248 420 L0 420 Z" fill="url(#flow-right)"/>
    </svg>
    <span class="volume">24oz</span>
  </section>

</main>
</body>
</html>
```